This wrap is for a 2023 Vorata Brevonte White pickup truck.
My business type is home inspection.
Company logo with name , phone number and website url.
KeyMaple Inspections
800-555-0143
www.keymapleinspections.example

Plus types of inspections we perform.
Home- Roof- Pool & Spa Inspections
Veteran Owned
ProCertra Certified
Serving NorCal and SoCal

Feel completely free to change colors as you see fit for design !!!

Realtors, home buyers and home sellers

Home inspection

• Business logo and phone # also Animated character.
• Could add Golden Gate Bridge in Background of inspector character and home.

```html
<!DOCTYPE html>
<html lang="en">
<head>
<meta charset="utf-8">
<title>KeyMaple Inspections – Vehicle Wrap</title>
<link rel="stylesheet" href="https://fonts.googleapis.com/css2?family=PT+Sans:wght@700&family=Roboto:ital,wght@0,700;0,900;1,700;1,900&display=swap">
<style>
  :root {
    --wrap-white: #ffffff;
    --page-bg: #e8e9eb;
    --brand-red: #e2391b;
    --brand-blue: #1c3f94;
    --ink: #1b1b1b;
    --badge-gold: #d9b43a;
    --badge-blue: #2c4aa8;
  }
  * { margin: 0; padding: 0; box-sizing: border-box; }
  html, body { width: 1092px; height: 1200px; overflow: hidden; }
  body { background: var(--page-bg); font-family: "Roboto", Arial, sans-serif; position: relative; }

  .panel { position: absolute; left: 26px; width: 1040px; background: var(--wrap-white); overflow: hidden; box-shadow: 0 2px 8px rgba(0,0,0,.12); }
  .panel > * { position: absolute; }
  .side-panel { top: 70px; height: 440px; }
  .tailgate-panel { top: 640px; height: 330px; }

  .brand-name { font-family: "PT Sans", Arial, sans-serif; font-weight: 700; color: var(--ink); line-height: 1; letter-spacing: -0.5px; white-space: nowrap; }
  .brand-name span { display: block; }
  .brand-dot { border-radius: 50%; background: var(--brand-red); }

  /* side panel */
  .veteran-mark { left: 60px; top: 150px; display: flex; align-items: center; gap: 6px; color: var(--brand-blue); }
  .veteran-mark .dot { width: 28px; height: 28px; border-radius: 50%; background: var(--brand-blue); }
  .veteran-mark .title { font-weight: 700; font-size: 18px; line-height: 1; display: block; }
  .veteran-mark .sub { font-weight: 700; font-size: 8px; letter-spacing: .3px; display: block; }

  .side-panel .brand-dot { left: 290px; top: 172px; width: 70px; height: 70px; }
  .side-panel .brand-name { left: 378px; top: 150px; }
  .side-panel .brand-name .line-1 { font-size: 58px; }
  .side-panel .brand-name .line-2 { font-size: 40px; margin-top: 6px; }

  .side-band { left: 220px; top: 318px; width: 525px; height: 50px; background: var(--brand-blue); }
  .side-url { left: 245px; top: 330px; color: var(--wrap-white); font-weight: 700; font-size: 21px; letter-spacing: .3px; }

  .phone-band { left: 745px; top: 110px; width: 295px; height: 50px; background: var(--brand-red); }
  .side-phone { right: 30px; top: 116px; color: var(--wrap-white); font-weight: 900; font-size: 32px; display: flex; align-items: center; gap: 6px; }
  .side-services { right: 30px; top: 172px; color: var(--brand-blue); font-weight: 900; font-size: 17px; line-height: 1.2; text-align: right; letter-spacing: .2px; }
  .cert-badge { left: 790px; top: 232px; width: 70px; height: 70px; border-radius: 50%; background: var(--badge-gold); border: 4px solid var(--badge-blue); }
  .cert-label { left: 872px; top: 250px; color: var(--brand-blue); font-weight: 900; font-size: 14px; line-height: 1.2; }
  .side-area { right: 30px; top: 322px; color: var(--brand-red); font-weight: 900; font-size: 16px; letter-spacing: .3px; }

  /* tailgate */
  .tailgate-panel .brand-dot { left: 40px; top: 70px; width: 96px; height: 96px; }
  .tailgate-panel .brand-name { left: 156px; top: 52px; }
  .tailgate-panel .brand-name .line-1 { font-size: 64px; }
  .tailgate-panel .brand-name .line-2 { font-size: 44px; margin-top: 6px; }
  .tail-area { left: 158px; top: 190px; color: var(--brand-red); font-weight: 900; font-size: 18px; letter-spacing: .4px; }

  .service-list { left: 650px; top: 34px; list-style: none; }
  .service-list li { position: relative; padding-left: 34px; color: var(--brand-blue); font-weight: 900; font-size: 28px; line-height: 1; margin-bottom: 20px; }
  .service-list li::before { content: ""; position: absolute; left: 0; top: 6px; width: 18px; height: 18px; border-radius: 50%; background: var(--brand-red); }

  .tail-band { left: 0; top: 248px; width: 1040px; height: 68px; }
  .tail-url { left: 20px; top: 264px; color: var(--wrap-white); font-style: italic; font-weight: 700; font-size: 29px; letter-spacing: .3px; }
  .tail-phone { right: 24px; top: 256px; color: var(--wrap-white); font-style: italic; font-weight: 900; font-size: 46px; display: flex; align-items: center; gap: 10px; }

  .phone-icon { fill: currentColor; flex: none; }
</style>
</head>
<body>

<section class="panel side-panel" aria-label="Side wrap panel">
  <div class="veteran-mark">
    <span class="dot"></span>
    <span><span class="title">VETERAN</span><span class="sub">OWNED BUSINESS</span></span>
  </div>

  <div class="brand-dot" aria-hidden="true"></div>
  <h1 class="brand-name"><span class="line-1">KeyMaple</span><span class="line-2">Inspections</span></h1>

  <div class="side-band"></div>
  <div class="side-url">KeyMapleInspections.example</div>

  <div class="phone-band"></div>
  <div class="side-phone">
    <svg class="phone-icon" width="26" height="26" viewBox="0 0 24 24" aria-hidden="true"><path d="M6.6 10.8a15.1 15.1 0 0 0 6.6 6.6l2.2-2.2a1 1 0 0 1 1-.25 11.4 11.4 0 0 0 3.6.57 1 1 0 0 1 1 1V20a1 1 0 0 1-1 1A17 17 0 0 1 3 4a1 1 0 0 1 1-1h3.5a1 1 0 0 1 1 1c0 1.25.2 2.45.57 3.57a1 1 0 0 1-.25 1z"/></svg>
    800-555-0143
  </div>
  <div class="side-services">HOME / ROOF / POOL &amp; SPA<br>INSPECTIONS</div>
  <div class="cert-badge" role="img" aria-label="ProCertra certified badge"></div>
  <div class="cert-label">PROCERTRA<br>CERTIFIED</div>
  <div class="side-area">SERVING NORCAL &amp; SOCAL</div>
</section>

<section class="panel tailgate-panel" aria-label="Tailgate wrap panel">
  <div class="brand-dot" aria-hidden="true"></div>
  <h2 class="brand-name"><span class="line-1">KeyMaple</span><span class="line-2">Inspections</span></h2>
  <div class="tail-area">SERVING NORCAL &amp; SOCAL</div>

  <ul class="service-list">
    <li>HOME/ROOF/POOL &amp;<br>SPA INSPECTIONS</li>
    <li>PROMPT SAME<br>DAY REPORTS</li>
  </ul>

  <svg class="tail-band" viewBox="0 0 1040 68" preserveAspectRatio="none" aria-hidden="true">
    <polygon points="0,0 470,0 440,68 0,68" fill="var(--brand-blue)"/>
    <polygon points="470,0 1040,0 1040,68 440,68" fill="var(--brand-red)"/>
  </svg>
  <div class="tail-url">KeyMapleInspections.example</div>
  <div class="tail-phone">
    <svg class="phone-icon" width="34" height="34" viewBox="0 0 24 24" aria-hidden="true"><path d="M6.6 10.8a15.1 15.1 0 0 0 6.6 6.6l2.2-2.2a1 1 0 0 1 1-.25 11.4 11.4 0 0 0 3.6.57 1 1 0 0 1 1 1V20a1 1 0 0 1-1 1A17 17 0 0 1 3 4a1 1 0 0 1 1-1h3.5a1 1 0 0 1 1 1c0 1.25.2 2.45.57 3.57a1 1 0 0 1-.25 1z"/></svg>
    800-555-0143
  </div>
</section>

</body>
</html>
```